Small Firewood bag design (for use it retail stores NZ)

Hi, we are a small business in New Zealand selling firewood. We have started to bag our wood and are now selling to stores in NZ. We are in need of a good firewood bag design. The overall size to be 40cm high x 25cm wide, however the text should be at minimum 2cm within this, as to prevent it from going around the corner of the bag.
We will only be printing the label on 1 side of the bag, and would like a design for black printing only and a design with black and orange/flame color.
Our business is called 'Kettle Ridge Firewood', (KRF Limited)
The product/wood type is Black Wattle.
The wood is a very hardwood, makes a great burner, burns hot and long, especially when compared to pine.
Our firewood is naturally seasoned outside in the northland sun.
Black wattle is of the Acacia family from Australia.
The bags are only small, 12kg or 25 litres.
It will be printed onto clear woven PP bags, see image. So intricate drawings is not recommended.
There will be no barcode on the label, as this will be sewn onto the bag separately.
Can provide our contact details for the bag later.

Note, the below images I designed on an online AI program, but do quite like the look of them.

Target Market(s)

Will be for sale in large department stores, petrol stations, some liquor stores and some dairy's. Target market is older people, people going to the batch, wood for people not organized to get in bulk amounts of wood

Industry/Entity Type

Firewood, home heating, winter, cold

Colors

Designer to choose colors to be used in the design.

Requirements
Nice to have
• Possibly an image of logs with the flames around it

```html
<!DOCTYPE html>
<html lang="en">
<head>
<meta charset="utf-8">
<title>Kettle Ridge Firewood – Bag Label</title>
<link rel="stylesheet" href="https://fonts.googleapis.com/css2?family=Kaushan+Script&family=Roboto:wght@900&display=block">
<style>
  :root {
    --page: #ffffff;
    --label-black: #201c1d;
    --flame-orange: #f0861c;
    --flame-deep: #d8721a;
    --flame-ember: #5e3a1c;
    --ink-dark: #332a28;
  }
  html, body {
    margin: 0;
    padding: 0;
    width: 1200px;
    height: 1200px;
    overflow: hidden;
    background: var(--page);
  }
  .canvas {
    position: relative;
    width: 1200px;
    height: 1200px;
  }
  .bag-label {
    position: absolute;
    left: 285px;
    top: 60px;
    width: 630px;
    height: 1074px;
    display: block;
  }
  .label-ground { fill: var(--label-black); }
  .brand-name {
    font-family: "Kaushan Script", "Yellowtail", cursive;
    font-size: 150px;
    fill: var(--flame-orange);
  }
  .company-entity {
    font-family: "Roboto", Arial, sans-serif;
    font-weight: 900;
    font-size: 74px;
    fill: var(--ink-dark);
  }
</style>
</head>
<body>
  <div class="canvas">
    <svg class="bag-label" viewBox="0 0 630 1074" xmlns="http://www.w3.org/2000/svg">
      <defs>
        <linearGradient id="flameTones" x1="0" y1="0" x2="0" y2="1">
          <stop offset="0" stop-color="#201c1d" stop-opacity="0"/>
          <stop offset="0.12" stop-color="#3a2618"/>
          <stop offset="0.3" stop-color="#8a4f1a"/>
          <stop offset="0.45" stop-color="#f0861c"/>
          <stop offset="0.7" stop-color="#f0861c"/>
          <stop offset="0.85" stop-color="#d8721a"/>
          <stop offset="1" stop-color="#f0861c"/>
        </linearGradient>
      </defs>
      <rect class="label-ground" x="0" y="0" width="630" height="1074"/>
      <rect class="flame-field" x="0" y="500" width="630" height="574" fill="url(#flameTones)" role="img" aria-label="Illustration of orange flames rising from the bottom of the label"/>
      <text class="brand-name">
        <tspan x="30" y="226">Kettle</tspan>
        <tspan x="220" y="368">Ridge</tspan>
        <tspan x="20" y="493">Firewood</tspan>
      </text>
      <text class="company-entity" x="315" y="903" text-anchor="middle">KRF Limited</text>
    </svg>
  </div>
</body>
</html>
```